Postcard Design

I have an accounting firm and I would like to increase my customer base by a postcard mailout/letter dropI want a design that is eye catching and uses my logo. I specialise in small to medium business and offer services for commercial accounting and business advisory. I also want to offer a discount for new clients.Previously I had my website updated and would like to stay with the theme

Industry/Entity Type

Business Consultant

Font styles to use
Serif

Colors
b667aa
d3a5cc

Requirements
Must have
• the post card needs to be arty to attract attention. also business like

```html
<!DOCTYPE html>
<html lang="en">
<head>
<meta charset="utf-8">
<title>Lumora Accounting Services – Postcard</title>
<link rel="stylesheet" href="https://fonts.googleapis.com/css2?family=Arimo:wght@400;700&family=Tinos&family=Jost:wght@400;500&display=swap">
<style>
  :root {
    --backdrop: #231f20;
    --plum-deep: #7b4488;
    --plum: #9c55a6;
    --plum-light: #a65cb0;
    --orchid: #b667aa;
    --orchid-pale: #d3a5cc;
    --magenta-band: #a4379b;
    --tab: #b9659f;
    --heading-ink: #5a2a60;
    --ink: #333;
    --white: #fff;
  }
  * { box-sizing: border-box; margin: 0; padding: 0; }
  html, body { width: 894px; height: 1200px; overflow: hidden; }
  body { background: var(--backdrop); position: relative; font-family: "Arimo", Arial, sans-serif; }

  .card { position: absolute; left: 39px; width: 816px; height: 521px; background: var(--plum); overflow: hidden; }
  .card--front { top: 62px; }
  .card--back { top: 615px; }
  .card__wave { position: absolute; inset: 0; width: 100%; height: 100%; }

  .brand-tile {
    position: absolute; left: 18px; top: 0; width: 140px; height: 148px;
    background: var(--white); border-radius: 0 0 14px 14px;
    display: flex; flex-direction: column; align-items: center; justify-content: center; gap: 10px;
  }
  .brand-tile__dot { width: 56px; height: 56px; border-radius: 50%; background: var(--orchid); }
  .brand-tile__name { font-family: "Arimo", Arial, sans-serif; font-weight: 700; font-size: 18px; color: var(--orchid); }

  .front-title { position: absolute; left: 161px; top: 24px; font-weight: 700; font-size: 41px; color: var(--white); white-space: nowrap; letter-spacing: 0.2px; }
  .front-hours { position: absolute; right: 57px; top: 76px; font-weight: 700; font-size: 22px; line-height: 27px; color: var(--white); text-align: left; }

  .service-panel {
    position: absolute; top: 168px; height: 340px; background: var(--white);
    border: 2px solid var(--orchid); border-bottom: none; border-radius: 14px 14px 0 0;
  }
  .service-panel--commercial { left: 32px; width: 351px; }
  .service-panel--advisory { left: 419px; width: 371px; }
  .service-panel__tab {
    position: absolute; left: -3px; height: 23px; padding-left: 9px; line-height: 23px;
    font-weight: 700; font-size: 13.5px; color: var(--heading-ink);
    background: var(--tab); clip-path: polygon(0 0, 100% 0, 96% 100%, 0 100%);
  }
  .service-panel--commercial .service-panel__tab { top: 12px; width: 273px; }
  .service-panel--advisory .service-panel__tab { top: 20px; width: 276px; }
  .service-list { list-style: none; position: absolute; left: 8px; right: 10px; font-size: 14px; line-height: 17px; color: var(--ink); }
  .service-panel--commercial .service-list { top: 48px; }
  .service-panel--advisory .service-list { top: 56px; }
  .service-list li { position: relative; padding-left: 15px; margin-bottom: 5px; }
  .service-list li::before { content: "-"; position: absolute; left: 0; }

  .front-footer {
    position: absolute; left: 0; right: 0; bottom: 0; height: 40px; background: var(--magenta-band);
    color: var(--white); font-weight: 700; font-size: 11.6px; line-height: 14px; padding: 6px 8px;
  }
  .social-row { position: absolute; display: flex; }
  .social-row--small { right: 34px; top: 9px; gap: 6px; }
  .social-row--small .social-tile { width: 22px; height: 22px; border: 1.5px solid var(--white); border-radius: 3px; }
  .social-row--large { left: 396px; top: 378px; gap: 3px; }
  .social-row--large .social-tile { width: 39px; height: 42px; border: 2px solid var(--white); border-radius: 7px; }

  .back-title { position: absolute; left: 182px; top: 20px; font-weight: 700; font-size: 45px; color: var(--white); white-space: nowrap; }
  .back-subtitle {
    position: absolute; left: 183px; top: 70px; width: 426px; display: flex; align-items: center; gap: 8px;
    font-family: "Jost", sans-serif; font-size: 36px; letter-spacing: 6px; color: var(--white);
  }
  .back-subtitle::before, .back-subtitle::after { content: ""; flex: 1; height: 4px; background: var(--white); }
  .stamp-box { position: absolute; left: 704px; top: 25px; width: 104px; height: 127px; background: var(--white); }
  .back-intro {
    position: absolute; left: 37px; top: 183px; width: 660px;
    font-family: "Tinos", "Times New Roman", serif; font-size: 19.5px; line-height: 23.5px; color: var(--white);
  }
  .back-divider { position: absolute; left: 39px; top: 306px; width: 637px; height: 7px; background: var(--orchid-pale); }
  .back-contact { position: absolute; left: 36px; top: 334px; font-family: "Jost", sans-serif; color: var(--white); font-size: 18px; line-height: 21.5px; }
  .back-contact__phone { font-size: 29px; line-height: 36px; margin-top: 1px; }
  .back-contact__email { font-size: 16.5px; line-height: 20px; }
  .address-box { position: absolute; left: 631px; top: 405px; width: 167px; height: 71px; background: var(--white); }
  .address-band { position: absolute; left: 3px; top: 476px; width: 813px; height: 35px; background: var(--white); }
</style>
</head>
<body>

<section class="card card--front" aria-label="Postcard front">
  <svg class="card__wave" viewBox="0 0 816 521" preserveAspectRatio="none" aria-hidden="true">
    <rect width="816" height="521" fill="var(--plum)"/>
    <path d="M0 0H816V150C700 170 560 160 430 185C300 210 150 215 0 195Z" fill="var(--plum-deep)"/>
    <path d="M0 195C150 215 300 210 430 185C560 160 700 170 816 150V175C700 190 560 190 430 210C300 230 150 230 0 220Z" fill="var(--plum-light)" opacity="0.6"/>
  </svg>

  <div class="brand-tile"><span class="brand-tile__dot"></span><span class="brand-tile__name">Lumora</span></div>
  <h1 class="front-title">Lumora Accounting Services</h1>
  <p class="front-hours">Hours By Appointment<br>Telephone 02 40001234</p>

  <div class="service-panel service-panel--commercial">
    <h2 class="service-panel__tab">Commercial Accounting Services</h2>
    <ul class="service-list">
      <li>Accounting Procedures and Policies</li>
      <li>Audit Services, including Tier 1 and 2 Associations and Real Estate Trusts</li>
      <li>Budget Research, Preparation and Implementation</li>
      <li>Business Plans, Tailored to Your Business</li>
      <li>Cash Forecasting and Management</li>
      <li>General Ledger Reconciliations</li>
      <li>Payroll Administration</li>
      <li>Preparation of Financial and Management Reports</li>
      <li>Project Accounting, Property Development and Other Large Projects</li>
    </ul>
  </div>

  <div class="service-panel service-panel--advisory">
    <h2 class="service-panel__tab">Business Advisory – Compliance</h2>
    <ul class="service-list">
      <li>Business Development Solutions</li>
      <li>Business Structure and Set Up</li>
      <li>Certified Advisors for Innovative Software Add-Ons HR Consulting</li>
      <li>Registered ASIC Agent for Business Registration and Compliance Management</li>
      <li>Risk Management</li>
      <li>Self-Managed Superannuation Funds</li>
      <li>Tax Compliance – Registered BAS Agent</li>
    </ul>
  </div>

  <footer class="front-footer">
    Level 3, Suite 208 , 42 Harbour Lane, Newcastle, Australia 2300<br>
    Phone: +02 4000 1234 , Email: admin@lumoraaccounting.com
    <div class="social-row social-row--small" aria-label="Social links">
      <span class="social-tile"></span><span class="social-tile"></span><span class="social-tile"></span>
    </div>
  </footer>
</section>

<section class="card card--back" aria-label="Postcard back">
  <svg class="card__wave" viewBox="0 0 816 521" preserveAspectRatio="none" aria-hidden="true">
    <rect width="816" height="521" fill="var(--plum)"/>
    <path d="M0 0H816V110C690 120 560 115 430 140C300 165 150 165 0 150Z" fill="var(--plum-deep)"/>
    <path d="M0 150C150 165 300 165 430 140C560 115 690 120 816 110V135C690 140 560 145 430 165C300 185 150 185 0 175Z" fill="var(--plum-light)" opacity="0.6"/>
  </svg>

  <div class="brand-tile"><span class="brand-tile__dot"></span><span class="brand-tile__name">Lumora</span></div>
  <h1 class="back-title">Lumora Accounting</h1>
  <p class="back-subtitle">Services</p>
  <div class="stamp-box" aria-hidden="true"></div>

  <p class="back-intro">Our company is based on the belief that our customers' needs are of utmost importance. Lumora Accounting Services’ entire team is committed to meeting those needs. As a result, a high percentage of our business is from repeat customers and referrals in Newcastle, Australia.</p>
  <div class="back-divider"></div>

  <address class="back-contact" style="font-style:normal">
    Level 3, Suite 208<br>42 Harbour Lane<br>Newcastle, Australia 2300
    <div class="back-contact__phone">Phone: +02 4000 1234</div>
    <div class="back-contact__email">Email: admin@lumoraaccounting.com</div>
  </address>

  <div class="social-row social-row--large" aria-label="Social links">
    <span class="social-tile"></span><span class="social-tile"></span><span class="social-tile"></span>
  </div>

  <div class="address-box" aria-hidden="true"></div>
  <div class="address-band" aria-hidden="true"></div>
</section>

</body>
</html>
```